Capacity building in Resource Management

Need design of a business card (later to be completed by letterhead and webdesign in same fashion) for a professional who works in the field of capacity building of professionals in mostly developing countries in the field waste/resource management, waste prevention/reduction, cleaner production, stakeholders involvement, etc.
Info on business cards is to include provided logo, info in provided file and picture.

Industry/Entity Type

Business

Contact Information for Business Card

White background

Font styles to use
Sans Serif

Colors

Designer to choose colors to be used in the design.

```html
<!DOCTYPE html>
<html lang="en">
<head>
<meta charset="utf-8">
<title>terra-learna business card</title>
<link rel="stylesheet" href="https://fonts.googleapis.com/css2?family=Arimo:wght@400;700&display=swap">
<style>
  :root {
    --green: #4f8a3b;
    --green-dark: #2f5f25;
    --green-light: #5c9a45;
    --ink: #1c1c1c;
    --grey-text: #777;
    --rule: #d6d6d6;
    --paper: #ffffff;
    --backdrop: #a9a9a9;
  }
  * { margin: 0; padding: 0; box-sizing: border-box; }
  html, body { width: 1200px; height: 1200px; overflow: hidden; }
  body {
    background: var(--backdrop);
    font-family: "Arimo", Arial, sans-serif;
    position: relative;
  }
  .card {
    position: absolute;
    left: 160px;
    width: 880px;
    height: 502px;
    overflow: hidden;
    box-shadow: 0 6px 18px rgba(0,0,0,0.3);
  }
  .card-front { top: 68px; background: var(--paper); }
  .card-back {
    top: 630px;
    background: radial-gradient(ellipse at 55% 40%, var(--green-light) 0%, var(--green) 45%, var(--green-dark) 100%);
  }

  .brand-name {
    position: absolute;
    font-weight: 700;
    color: var(--green);
    letter-spacing: -0.5px;
    white-space: nowrap;
  }
  .card-front .brand-name { left: 60px; top: 70px; font-size: 44px; }
  .brand-dot {
    position: absolute;
    left: 60px; top: 44px;
    width: 18px; height: 18px;
    background: var(--green);
  }
  .tagline {
    position: absolute;
    right: 503px; top: 154px;
    text-align: right;
    font-size: 22px;
    line-height: 30px;
    color: var(--ink);
  }

  .portrait {
    position: absolute;
    left: 648px; top: 47px;
    width: 176px; height: 176px;
    border-radius: 50%;
    background: radial-gradient(circle at 45% 55%, #b98a6e 0%, #7a8a6a 45%, #3f5a3a 100%);
  }

  .person {
    position: absolute;
    right: 57px; top: 238px;
    white-space: nowrap;
  }
  .person-name { font-size: 32px; font-weight: 700; color: var(--green-dark); }
  .person-role { font-size: 22px; color: var(--grey-text); margin-left: 16px; letter-spacing: 0.5px; }

  .divider {
    position: absolute;
    left: 60px; top: 292px;
    width: 763px; height: 2px;
    background: var(--rule);
  }

  .contact-list {
    position: absolute;
    top: 322px;
    list-style: none;
    font-size: 25px;
    line-height: 34.5px;
    color: var(--ink);
  }
  .contact-list.primary { left: 60px; }
  .contact-list.social { left: 584px; }
  .contact-list li { display: flex; align-items: center; white-space: nowrap; }
  .contact-list svg { width: 20px; height: 20px; margin-right: 12px; flex: none; fill: var(--green-dark); }
  .social-dot {
    width: 14px; height: 14px; border-radius: 50%;
    background: var(--green-dark);
    margin: 0 16px 0 4px; flex: none;
  }

  .address {
    position: absolute;
    left: 0; right: 0; top: 448px;
    text-align: center;
    font-size: 25px;
    color: var(--ink);
  }
  .footer-band { position: absolute; left: 0; bottom: 0; width: 880px; height: 20px; }

  .card-back .brand-name {
    left: 0; right: 80px; top: 232px;
    text-align: right;
    font-size: 92px;
    color: var(--paper);
    letter-spacing: -1px;
  }
  .card-back .back-tagline {
    position: absolute;
    right: 104px; top: 340px;
    font-size: 21px;
    color: var(--paper);
  }
</style>
</head>
<body>

<section class="card card-front">
  <span class="brand-dot"></span>
  <div class="brand-name">terra-learna</div>
  <p class="tagline">Capacity Building in<br>Resource Management</p>

  <div class="portrait" role="img" aria-label="Portrait photo of the director"></div>

  <div class="person">
    <span class="person-name">Joren Valkema</span><span class="person-role">DIRECTOR</span>
  </div>

  <div class="divider"></div>

  <ul class="contact-list primary">
    <li>
      <svg viewBox="0 0 24 24" aria-hidden="true"><path d="M6.6 10.8a15.1 15.1 0 0 0 6.6 6.6l2.2-2.2a1 1 0 0 1 1-.25 11.4 11.4 0 0 0 3.6.57 1 1 0 0 1 1 1V20a1 1 0 0 1-1 1A17 17 0 0 1 3 4a1 1 0 0 1 1-1h3.5a1 1 0 0 1 1 1c0 1.25.2 2.45.57 3.57a1 1 0 0 1-.25 1z"/></svg>
      +49 1500 555 0142
    </li>
    <li>
      <svg viewBox="0 0 24 24" aria-hidden="true"><path d="M2 5h20v14H2z M2 5l10 8 10-8" fill="none" stroke="#2f5f25" stroke-width="0"/><path d="M2 6.5l10 7 10-7V19H2z"/><path d="M2 5h20l-10 7z"/></svg>
      joren.valkema@terra-learna.com
    </li>
    <li>
      <svg viewBox="0 0 24 24" aria-hidden="true"><circle cx="12" cy="12" r="10"/><path d="M2 12h20M12 2v20M5 6.5h14M5 17.5h14" stroke="#fff" stroke-width="1.4" fill="none"/><ellipse cx="12" cy="12" rx="4.5" ry="10" stroke="#fff" stroke-width="1.4" fill="none"/></svg>
      www.terra-learna.com
    </li>
  </ul>

  <ul class="contact-list social">
    <li><span class="social-dot"></span>@jorenvalkema</li>
    <li><span class="social-dot"></span>valk2010</li>
    <li><span class="social-dot"></span>Joren Valkema</li>
  </ul>

  <p class="address">Lindenweg 12, 10117 Berlin, Germany</p>

  <svg class="footer-band" viewBox="0 0 880 20" aria-hidden="true">
    <path d="M126 20 C126 6 140 0 170 0 H712 C742 0 756 6 756 20 Z" fill="var(--green-dark)"/>
    <path d="M150 20 C150 10 160 5 185 5 H697 C722 5 732 10 732 20 Z" fill="var(--green)"/>
  </svg>
</section>

<section class="card card-back">
  <div class="brand-name">terra-learna</div>
  <p class="back-tagline">capacity building in resource management</p>
</section>

</body>
</html>
```